Powerpoint template (PPT) for investment company
based on website theme
Powerpoint template (PPT) for investment company - Financial Services
Creative Brief
Use specific fonts
Please choose as long as it look professional
Simple
Please check the website
Please check from the website
tpaxwell@fernmail.net
Please create the powerpoint template based on our new website which is at http://kovalpartners.client.sitebramble.net Ideally we want the background design of the template have similar look and feel as our new website to keep the brand identity. We would like the powerpoint template with our logo that we can use for our marketing presentations. The template would have a template for the title slide and a template for remaining slides in the presentation. The font would be standardized throughout so each member of our team could easily plug in their information and the font size, type, and color would be consistent for all our presentations. The template should be built as a PowerPoint template file and be compatible with Microsoft Office 2010 or 2013, using the “.pot” file extension. The template slide layouts should include (at least): title and text block; title and bulleted text (with multiple bullet levels); title and content; and title and graph (e.g. bar chart, with default colors matching the overall template design). If possible, we would like submissions to include one option for the design with a dark background and another option with a light background (to accommodate preferences of the different presenters in our group).

```html
<!DOCTYPE html>
<html lang="en">
<head>
<meta charset="utf-8">
<title>Koval Partners – Presentation Template, Dark Version</title>
<link rel="stylesheet" href="https://fonts.googleapis.com/css2?family=Cinzel:wght@400;600&family=Open+Sans:wght@400;600;700&display=swap">
<style>
  :root{
    --stage:#000000;
    --note:#ffffff;
    --slide-top:#f6f6f6;
    --slide-bottom:#d9d9d9;
    --dark-top:#cfcfcf;
    --dark-bottom:#9e9e9e;
    --strip:#c4c4c4;
    --strip-dark:#8e8e8e;
    --ink:#3b3b3b;
    --ink-soft:#6a6a6a;
    --text:#707070;
    --band:#ffffff;
    --footer:#f2f2f2;
    --orange:#f39200;
    --blue:#2f80c8;
    --green:#4fae3c;
    --red:#d8262c;
    --yellow:#f2c515;
    --map-a:#b9b9b9;
    --map-b:#e6e6e6;
  }
  *{box-sizing:border-box;margin:0;padding:0}
  html,body{width:1200px;height:646px;overflow:hidden;background:var(--stage)}
  body{position:relative;font-family:"Open Sans",Arial,sans-serif}

  .board-note{position:absolute;left:46px;top:20px;color:var(--note);font-size:15px;font-weight:700}

  .slide{position:absolute;width:350px;height:256px;overflow:hidden;
    background:linear-gradient(var(--slide-top),var(--slide-bottom))}
  .slide--dark{background:linear-gradient(var(--dark-top),var(--dark-bottom))}
  .slide--a{left:46px;top:62px}
  .slide--b{left:425px;top:62px}
  .slide--c{left:804px;top:62px}
  .slide--d{left:228px;top:348px}
  .slide--e{left:622px;top:348px}

  .top-strip{position:absolute;left:0;top:0;width:100%;height:12px;
    background:linear-gradient(90deg,var(--strip) 0 62%,var(--strip-dark) 62% 100%)}

  .footer{position:absolute;left:0;bottom:0;width:100%;height:24px;background:var(--footer);
    display:flex;align-items:center;justify-content:space-between;padding-left:12px}
  .footer__url{font-size:8px;color:var(--ink-soft)}
  .footer__page{height:100%;width:34px;background:var(--orange);color:#fff;font-size:8px;
    display:flex;align-items:center;justify-content:center}

  /* title slides */
  .title-hero{position:absolute;left:0;top:12px;width:100%;height:140px}
  .title-hero__map{position:absolute;right:0;top:0;width:230px;height:140px;
    background:radial-gradient(ellipse at 55% 50%,var(--map-a),rgba(0,0,0,0) 70%)}
  .slide--dark .title-hero__map{background:radial-gradient(ellipse at 55% 50%,#8a8a8a,rgba(0,0,0,0) 70%)}
  .brand{position:absolute;left:18px;top:30px;font-family:"Cinzel",Georgia,serif;font-size:25px;color:var(--ink);letter-spacing:1px}
  .title-band{position:absolute;left:0;top:150px;width:100%;height:64px;background:var(--band);padding:12px 18px}
  .slide--dark .title-band{background:#e4e4e4}
  .title-band__title{font-family:"Cinzel",Georgia,serif;font-size:19px;color:var(--ink);line-height:1.1}
  .title-band__desc{font-family:"Cinzel",Georgia,serif;font-size:13px;color:var(--orange);line-height:1.2}

  /* content slides */
  .content-head{position:absolute;left:12px;top:18px;right:12px}
  .content-head__title{font-family:"Cinzel",Georgia,serif;font-weight:600;font-size:11.5px;color:var(--ink);white-space:nowrap}
  .content-head__sub{font-size:6.5px;color:var(--ink-soft)}
  .body-copy{font-size:6px;line-height:1.45;color:var(--text)}

  .text-chart{position:absolute;left:12px;top:52px;right:12px;display:flex;gap:12px}
  .text-chart .body-copy{width:150px}
  .bar-chart{width:166px;height:110px}

  .groups{position:absolute;left:14px;top:56px;right:14px;display:grid;grid-template-columns:1fr 1fr;gap:10px 18px}
  .group{display:flex;gap:6px}
  .group__arrow{flex:none;margin-top:2px}
  .group__name{font-family:"Cinzel",Georgia,serif;font-weight:600;font-size:8px;color:var(--ink)}
  .group__note{font-size:5.5px;line-height:1.4;color:var(--text)}

  .process-copy{position:absolute;left:12px;top:52px;right:12px}
  .process{position:absolute;left:12px;top:132px;width:326px;height:40px}
  .process text{font-family:"Open Sans",Arial,sans-serif;font-size:6px;fill:#fff}
</style>
</head>
<body>
  <p class="board-note">Here is dark version, I think light one looks better 1 your choice.</p>

  <!-- Title slide, dark -->
  <section class="slide slide--a slide--dark">
    <div class="top-strip"></div>
    <div class="title-hero">
      <div class="title-hero__map" role="img" aria-label="Faint world map background"></div>
      <div class="brand">Koval Partners</div>
    </div>
    <div class="title-band">
      <h1 class="title-band__title">Presentation Title</h1>
      <p class="title-band__desc">Description Here</p>
    </div>
    <footer class="footer"><span class="footer__url">www.kovalpartners.com</span><span class="footer__page">Pg#1</span></footer>
  </section>

  <!-- Title slide, light -->
  <section class="slide slide--b">
    <div class="top-strip"></div>
    <div class="title-hero">
      <div class="title-hero__map" role="img" aria-label="Faint world map background"></div>
      <div class="brand">Koval Partners</div>
    </div>
    <div class="title-band">
      <h1 class="title-band__title">Presentation Title</h1>
      <p class="title-band__desc">Description Here</p>
    </div>
    <footer class="footer"><span class="footer__url">www.kovalpartners.com</span><span class="footer__page">Pg#1</span></footer>
  </section>

  <!-- Title, text and chart -->
  <section class="slide slide--c">
    <div class="top-strip"></div>
    <header class="content-head">
      <h2 class="content-head__title">Slide Title Goes Here | Slide Title Goes Here</h2>
      <p class="content-head__sub">Slide Subtitle Goes Here</p>
    </header>
    <div class="text-chart">
      <p class="body-copy">Our investment approach combines careful research with long term discipline. We review each holding every quarter and report results to clients in plain language. Portfolios are built around clear goals, measured risk and steady growth, with fees that stay simple and visible at all times.</p>
      <svg class="bar-chart" viewBox="0 0 166 110" aria-label="Bar chart">
        <g stroke="#bdbdbd" stroke-width="0.5">
          <line x1="10" y1="10" x2="162" y2="10"/><line x1="10" y1="35" x2="162" y2="35"/>
          <line x1="10" y1="60" x2="162" y2="60"/><line x1="10" y1="85" x2="162" y2="85"/>
        </g>
        <line x1="10" y1="100" x2="162" y2="100" stroke="#888" stroke-width="0.8"/>
        <g>
          <rect x="14" y="60" width="5" height="40" fill="var(--blue)"/><rect x="19" y="45" width="5" height="55" fill="var(--green)"/><rect x="24" y="70" width="5" height="30" fill="var(--red)"/><rect x="29" y="55" width="5" height="45" fill="var(--orange)"/><rect x="34" y="75" width="5" height="25" fill="var(--yellow)"/>
          <rect x="52" y="40" width="5" height="60" fill="var(--blue)"/><rect x="57" y="55" width="5" height="45" fill="var(--green)"/><rect x="62" y="30" width="5" height="70" fill="var(--red)"/><rect x="67" y="62" width="5" height="38" fill="var(--orange)"/><rect x="72" y="50" width="5" height="50" fill="var(--yellow)"/>
          <rect x="90" y="25" width="5" height="75" fill="var(--blue)"/><rect x="95" y="48" width="5" height="52" fill="var(--green)"/><rect x="100" y="58" width="5" height="42" fill="var(--red)"/><rect x="105" y="35" width="5" height="65" fill="var(--orange)"/><rect x="110" y="66" width="5" height="34" fill="var(--yellow)"/>
          <rect x="128" y="52" width="5" height="48" fill="var(--blue)"/><rect x="133" y="20" width="5" height="80" fill="var(--green)"/><rect x="138" y="44" width="5" height="56" fill="var(--red)"/><rect x="143" y="28" width="5" height="72" fill="var(--orange)"/><rect x="148" y="58" width="5" height="42" fill="var(--yellow)"/>
        </g>
      </svg>
    </div>
    <footer class="footer"><span class="footer__url">www.kovalpartners.com</span><span class="footer__page">Pg#1</span></footer>
  </section>

  <!-- Title and bulleted groups -->
  <section class="slide slide--d">
    <div class="top-strip"></div>
    <header class="content-head">
      <h2 class="content-head__title">Slide Title Goes Here | Slide Title Goes Here</h2>
      <p class="content-head__sub">Slide Subtitle Goes Here</p>
    </header>
    <ul class="groups">
      <li class="group"><svg class="group__arrow" width="7" height="8" viewBox="0 0 7 8"><path d="M0 0L7 4L0 8Z" fill="var(--orange)"/></svg><div><p class="group__name">Group 1</p><p class="group__note">Short note about this group and the services it offers clients.</p></div></li>
      <li class="group"><svg class="group__arrow" width="7" height="8" viewBox="0 0 7 8"><path d="M0 0L7 4L0 8Z" fill="var(--orange)"/></svg><div><p class="group__name">Group 1</p><p class="group__note">Short note about this group and the services it offers clients.</p></div></li>
      <li class="group"><svg class="group__arrow" width="7" height="8" viewBox="0 0 7 8"><path d="M0 0L7 4L0 8Z" fill="var(--orange)"/></svg><div><p class="group__name">Group 1</p><p class="group__note">Short note about this group and the services it offers clients.</p></div></li>
      <li class="group"><svg class="group__arrow" width="7" height="8" viewBox="0 0 7 8"><path d="M0 0L7 4L0 8Z" fill="var(--orange)"/></svg><div><p class="group__name">Group 1</p><p class="group__note">Short note about this group and the services it offers clients.</p></div></li>
      <li class="group"><svg class="group__arrow" width="7" height="8" viewBox="0 0 7 8"><path d="M0 0L7 4L0 8Z" fill="var(--orange)"/></svg><div><p class="group__name">Group 1</p><p class="group__note">Short note about this group and the services it offers clients.</p></div></li>
      <li class="group"><svg class="group__arrow" width="7" height="8" viewBox="0 0 7 8"><path d="M0 0L7 4L0 8Z" fill="var(--orange)"/></svg><div><p class="group__name">Group 1</p><p class="group__note">Short note about this group and the services it offers clients.</p></div></li>
    </ul>
    <footer class="footer"><span class="footer__url">www.kovalpartners.com</span><span class="footer__page">Pg#1</span></footer>
  </section>

  <!-- Title, text and process -->
  <section class="slide slide--e">
    <div class="top-strip"></div>
    <header class="content-head">
      <h2 class="content-head__title">Slide Title Goes Here | Slide Title Goes Here</h2>
      <p class="content-head__sub">Slide Subtitle Goes Here</p>
    </header>
    <p class="process-copy body-copy">This layout shows a simple process from first meeting to final review. Each step is a single phase of work, and the arrows below can hold short labels for the stages of your plan.</p>
    <svg class="process" viewBox="0 0 326 40" aria-label="Four step process arrows">
      <path d="M0 0H70L86 20L70 40H0Z" fill="var(--blue)"/>
      <path d="M80 0H150L166 20L150 40H80L96 20Z" fill="var(--green)"/>
      <path d="M160 0H230L246 20L230 40H160L176 20Z" fill="var(--red)"/>
      <path d="M240 0H310L326 20L310 40H240L256 20Z" fill="var(--orange)"/>
      <text x="26" y="22">Lorem ipsum</text>
      <text x="108" y="22">Lorem ipsum</text>
      <text x="188" y="22">Lorem ipsum</text>
      <text x="268" y="22">Lorem ipsum</text>
    </svg>
    <footer class="footer"><span class="footer__url">www.kovalpartners.com</span><span class="footer__page">Pg#1</span></footer>
  </section>
</body>
</html>
```